Custom Wine Label for Restaurant

Our restaurant needs to create a custom wine label to place on wine bottles. I would like the wine to be called "Gerald's Cask Dark" and have our logo and the sketch of him or a new one on the front. There are some mandatory legal items that must be on the label: The mandatory items for the KPF are ABV (13.5%), the government warning, the vinted and bottled by section with our location and website. I have included a sample label. I would like a front and back. The back can be lorem ipsum filler text for the time being. This should be a white label with the red logos/fonts used. I have also uploaded the sample labels to base the size and legal stuff off, they are under "Boston"
Restaurant, Bar, Wine
- Like the ones on the logos

```html
<!DOCTYPE html>
<html lang="en">
<head>
<meta charset="utf-8">
<title>Gerald's Cask Dark – Wine Labels</title>
<link rel="stylesheet" href="https://fonts.googleapis.com/css2?family=Jost:wght@400;600&family=Oswald:wght@500&display=swap">
<style>
  :root {
    --backdrop: #ebe8e5;
    --label-white: #ffffff;
    --brand-red: #e2442a;
    --ink: #1a1a1a;
    --sketch-dark: #3a3a3a;
    --sketch-light: #bdbdbd;
    --label-shadow: rgba(0, 0, 0, 0.12);
  }
  * { margin: 0; padding: 0; box-sizing: border-box; }
  html, body {
    width: 1200px;
    height: 1054px;
    overflow: hidden;
    background: var(--backdrop);
  }
  .label-sheet {
    width: 1200px;
    height: 1054px;
    display: flex;
    align-items: center;
    justify-content: center;
    gap: 66px;
  }
  .label {
    position: relative;
    width: 500px;
    height: 500px;
    background: var(--label-white);
    box-shadow: 0 6px 24px var(--label-shadow);
    color: var(--ink);
  }

  /* Front label */
  .front-label .wine-name {
    position: absolute;
    top: 40px;
    left: 0;
    right: 0;
    text-align: center;
    font-family: "Jost", sans-serif;
    font-weight: 600;
    font-size: 68px;
    line-height: 78px;
    color: var(--brand-red);
  }
  .front-label .portrait {
    position: absolute;
    top: 232px;
    left: 190px;
    width: 120px;
    height: 160px;
  }
  .front-label .vintage {
    position: absolute;
    top: 430px;
    left: 0;
    right: 0;
    display: flex;
    justify-content: center;
    align-items: center;
    gap: 14px;
    font-family: "Jost", sans-serif;
    font-weight: 400;
    font-size: 31px;
    letter-spacing: 3px;
  }
  .vintage .dot {
    width: 8px;
    height: 8px;
    border-radius: 50%;
    background: var(--brand-red);
  }

  /* Back label */
  .back-label .header {
    position: absolute;
    top: 24px;
    left: 44px;
    right: 60px;
    display: flex;
    align-items: center;
    gap: 32px;
  }
  .back-label .portrait {
    width: 70px;
    height: 96px;
    flex: none;
  }
  .back-label .wine-name {
    font-family: "Jost", sans-serif;
    font-weight: 600;
    font-size: 34px;
    line-height: 38px;
    color: var(--brand-red);
    text-align: center;
    flex: 1;
  }
  .back-label .story {
    position: absolute;
    top: 146px;
    left: 30px;
    right: 30px;
    text-align: center;
    font-family: "Jost", sans-serif;
    font-weight: 400;
    font-size: 15.5px;
    line-height: 24.3px;
  }
  .legal {
    position: absolute;
    left: 32px;
    right: 32px;
    top: 392px;
    font-family: "Oswald", sans-serif;
    font-weight: 500;
    text-transform: uppercase;
  }
  .legal .producer-row {
    display: flex;
    justify-content: space-between;
    align-items: flex-end;
    font-size: 11.5px;
    line-height: 15px;
    padding-bottom: 8px;
    border-bottom: 1.5px solid var(--ink);
  }
  .legal .producer {
    color: var(--brand-red);
  }
  .legal .warning {
    margin-top: 8px;
    font-size: 8.4px;
    line-height: 12px;
    letter-spacing: 0.1px;
  }
</style>
</head>
<body>
  <main class="label-sheet">
    <section class="label front-label">
      <h1 class="wine-name">Gerald's<br>Cask Dark</h1>
      <svg class="portrait" viewBox="0 0 120 160" role="img" aria-label="Ink sketch portrait of Gerald, the restaurant owner">
        <defs>
          <linearGradient id="sketch-tone-front" x1="0" y1="0" x2="0" y2="1">
            <stop offset="0" stop-color="var(--sketch-dark)"/>
            <stop offset="1" stop-color="var(--sketch-light)"/>
          </linearGradient>
        </defs>
        <rect width="120" height="160" fill="url(#sketch-tone-front)"/>
      </svg>
      <p class="vintage"><span class="dot"></span>2025<span class="dot"></span></p>
    </section>

    <section class="label back-label">
      <header class="header">
        <svg class="portrait" viewBox="0 0 70 96" role="img" aria-label="Small ink sketch portrait of Gerald">
          <defs>
            <linearGradient id="sketch-tone-back" x1="0" y1="0" x2="0" y2="1">
              <stop offset="0" stop-color="var(--sketch-dark)"/>
              <stop offset="1" stop-color="var(--sketch-light)"/>
            </linearGradient>
          </defs>
          <rect width="70" height="96" fill="url(#sketch-tone-back)"/>
        </svg>
        <h2 class="wine-name">Gerald's<br>Cask Dark</h2>
      </header>
      <p class="story">Lorem Ipsum Dolor Sit Amet, Consectetur Adipiscing Elit, Sed Do Eiusmod Tempor Incididunt Ut Labore Et Dolore Magna Aliqua. Ut Enim Ad Minim Veniam, Quis Nostrud Exercitation Ullamco Laboris Nisi Ut Aliquip Ex Ea Commodo Consequat. Duis Aute Irure Dolor In Reprehenderit In Voluptate Velit Esse Cillum Dolore Eu Fugiat Nulla Pariatur. Excepteur Sint Occaecat Cupidatat Non Proident, Sunt In Culpa Qui Officia Deserunt Mollit Anim Id Est Laborum</p>
      <footer class="legal">
        <div class="producer-row">
          <p>Vinted &amp; Bottled By<br><span class="producer">Gerald's Cask House - Boston</span></p>
          <p>Contains Sulfites: Alc.13.5% By Vol. 750ml</p>
        </div>
        <p class="warning">Government Warning: (1) According to the Surgeon General, women should not drink alcoholic beverages during pregnancy because of the risk of birth defects. (2) Consumption of alcoholic beverages impairs your ability to drive a car or operate machinery, and may cause health problems.</p>
      </footer>
    </section>
  </main>
</body>
</html>
```